24 hour coin operated Brisk Pulse Workout Hall Grand opening.

We are the first of our kind on the planet. I have invented and opened three 24 hour coin operated cardio centers. It's a gym with no weights and no classes. It only has cardio equipment. Imagine a laundromat or a video game arcade, only the machines are treadmills, cross trainers, stair steppers, bikes, etc. my sales person is a coin changer. I have no employees that work in the gym. It's fully automated. I am opening my fourth location and would like to announce its opening, while offering a special pre sale pricing for my tokens. The pre sale pricing is only good until about a week after I open and then the tokens will be regular price. The price is buy 40 tokens get 10 free. My opening day is expected to be Septmebr 14th, so bonus offer ends on the 22nd of Septemebr. I am hoping for a unique design to go along with our unique fitness style.

Target Market(s)

Men and Women from the ages of 14 to 65. all ages really.

Industry/Entity Type

Fitness

Font styles to use
Sans Serif

Colors
fbed22
000000

Requirements
Must have
• Our name and logo B Pulse Workout
• Our FB access name FB:BRISKPULSEWORKOUT
• Must say 24 hours
• Must say worlds first coin operated cardio center.
• Must say grand opening special offer ends Septemebr 22nd
• Phone number: 0958476201
• Must have our address and map:
• No.53, Linsen Rd., Beiyuan Dist., Tainan City 710 (see attached men for map)
Nice to have
• Website: briskpulsewkt.example
Should not have
• Please don't worry about the Chinese characters If I haven't asked you to add them. Sorry, this is to save time for those who haven't been selected.

```html
<!DOCTYPE html>
<html lang="en">
<head>
<meta charset="utf-8">
<title>Brisk Pulse Workout Hall – Grand Opening Flyers</title>
<link href="https://fonts.googleapis.com/css2?family=Anton&family=Montserrat:wght@800;900&family=Poppins:wght@400;500;600;700&display=swap" rel="stylesheet">
<style>
  :root{
    --yellow:#fbed22;
    --black:#000000;
    --ink:#111111;
    --blue:#1d3aa6;
    --red:#e3141b;
    --red-dark:#a80d12;
    --white:#ffffff;
    --stage:#2a2a2a;
    --gym-a:#3a3c40;
    --gym-b:#141517;
    --map:#c9c7c2;
    --panel:#505256;
  }
  *{box-sizing:border-box;margin:0;padding:0}
  html,body{width:1200px;height:850px;overflow:hidden}
  body{background:var(--stage);font-family:"Poppins",sans-serif;position:relative}

  .flyer{position:absolute;top:53px;width:525px;height:744px;overflow:hidden;background:var(--gym-b)}
  .flyer--front{left:52px}
  .flyer--back{left:624px}

  .flyer__backdrop{position:absolute;left:0;top:130px;width:525px;height:614px;
    background:linear-gradient(160deg,var(--gym-a),var(--gym-b) 70%)}
  .flyer__shapes{position:absolute;inset:0}

  .brand-mark{position:absolute;left:40px;top:30px;width:112px;height:112px;border-radius:50%;background:var(--black)}
  .brand-name{position:absolute;left:184px;top:26px;font-family:"Poppins",sans-serif;font-weight:700;font-size:31px;color:var(--blue);white-space:nowrap}
  .brand-tagline{position:absolute;left:250px;top:64px;font-weight:600;font-size:11.5px;color:var(--red);white-space:nowrap}

  .headline-first{position:absolute;left:184px;top:86px;font-family:"Montserrat",sans-serif;font-weight:900;font-size:35px;line-height:37px;color:var(--ink)}
  .headline-coin{position:absolute;left:44px;top:152px;font-family:"Anton",sans-serif;font-size:55px;line-height:60px;color:var(--red);white-space:nowrap}
  .headline-coin small{font-size:42px}
  .headline-center{position:absolute;left:44px;top:210px;font-family:"Montserrat",sans-serif;font-weight:900;font-size:35px;color:var(--red);white-space:nowrap}

  .badge-24{position:absolute;left:368px;top:112px;width:124px;height:124px;border-radius:50%;background:var(--red);
    border:4px solid var(--white);box-shadow:0 0 0 3px var(--red);color:var(--white);text-align:center;transform:rotate(-12deg)}
  .badge-24 .open{display:block;font-family:"Anton",sans-serif;font-size:22px;line-height:22px;margin-top:12px}
  .badge-24 .num{display:block;font-family:"Anton",sans-serif;font-size:56px;line-height:52px}
  .badge-24 .hours{display:block;font-family:"Anton",sans-serif;font-size:20px;line-height:20px}

  .opening-title{position:absolute;left:0;width:525px;text-align:center;top:286px;font-family:"Montserrat",sans-serif;font-weight:900;font-size:34px;color:var(--yellow)}
  .opening-sub{position:absolute;left:0;width:525px;text-align:center;top:326px;font-size:18px;font-weight:500;color:var(--white);letter-spacing:.5px}

  .location{position:absolute;left:45px;top:354px;width:460px;height:164px;border:3px solid var(--red);background:var(--panel);display:flex}
  .location__map{width:262px;height:100%;background:linear-gradient(135deg,#d4d2cc,var(--map))}
  .location__info{flex:1;position:relative;color:var(--white);text-align:right;padding:60px 14px 0 0;font-size:16.5px;line-height:24px}
  .location__pin{position:absolute;right:62px;top:8px}

  .offer-title{position:absolute;right:34px;top:548px;text-align:right;font-family:"Montserrat",sans-serif;font-weight:900;font-size:29px;line-height:34px;color:var(--white)}
  .offer-deal{position:absolute;left:36px;top:624px;font-family:"Anton",sans-serif;font-size:39px;color:var(--yellow);white-space:nowrap;text-shadow:2px 2px 0 var(--black)}
  .offer-deal b{font-weight:400;color:var(--white)}
  .offer-ends{position:absolute;left:36px;top:686px;font-size:13px;color:var(--white)}

  .phone{position:absolute;display:flex;align-items:center;gap:8px;font-family:"Montserrat",sans-serif;font-weight:900;color:var(--white);white-space:nowrap}
  .flyer--front .phone{right:34px;top:676px;font-size:26px}
  .flyer--back .phone{right:20px;top:666px;font-size:30px}

  .footer-web{position:absolute;display:flex;align-items:center;gap:8px;color:var(--white);font-weight:500;white-space:nowrap}
  .flyer--front .footer-web{left:36px;top:719px;font-size:15px}
  .flyer--back .footer-web{right:20px;top:706px;font-size:16px}
  .footer-follow{position:absolute;display:flex;align-items:center;gap:5px;font-size:10px;font-weight:600;white-space:nowrap}
  .footer-follow .dot{width:11px;height:11px;border-radius:50%;background:currentColor}
  .flyer--front .footer-follow{left:312px;top:725px;color:var(--ink)}
  .flyer--back .footer-follow{left:56px;top:714px;color:var(--white)}

  .steps-photo{position:absolute;left:52px;width:156px;height:102px;border:2px solid var(--white);background:linear-gradient(135deg,#b9a86a,#4b4a45)}
  .step{position:absolute;left:268px;width:210px;color:var(--white);font-size:13.5px;line-height:18px;border-bottom:1px solid var(--yellow);padding-bottom:10px}
  .step h3{font-size:14px;font-weight:700;color:var(--yellow);margin-bottom:8px}
</style>
</head>
<body>

<section class="flyer flyer--front">
  <div class="flyer__backdrop" role="img" aria-label="Dark photo of cardio machines in the gym"></div>
  <svg class="flyer__shapes" width="525" height="744" viewBox="0 0 525 744">
    <polygon points="0,0 525,0 525,140 0,282" fill="var(--yellow)"/>
    <polygon points="0,282 525,140 525,152 0,294" fill="#1a1a1a"/>
    <polygon points="0,595 525,515 525,744 0,744" fill="var(--red)"/>
    <polygon points="0,625 300,585 0,680" fill="var(--red-dark)" opacity=".6"/>
    <rect x="0" y="716" width="525" height="28" fill="var(--black)"/>
    <polygon points="305,716 525,716 525,744 295,744" fill="var(--yellow)"/>
  </svg>

  <div class="brand-mark"></div>
  <div class="brand-name">Brisk Pulse Workout</div>
  <div class="brand-tagline">BUILD YOUR BODY - BUILD YOUR DREAMS</div>
  <div class="headline-first">WORLDS<br>FIRST</div>
  <div class="headline-coin">COIN <small>OPERATED</small></div>
  <div class="headline-center">CARDIO CENTER</div>
  <div class="badge-24"><span class="open">Open</span><span class="num">24</span><span class="hours">Hours</span></div>

  <div class="opening-title">GRAND OPENING</div>
  <div class="opening-sub">NEAR YOUR LOCATION</div>

  <div class="location">
    <div class="location__map" role="img" aria-label="Street map showing the gym location"></div>
    <div class="location__info">
      <svg class="location__pin" width="30" height="40" viewBox="0 0 30 40"><path d="M15 1C7 1 1 7 1 15c0 10 14 24 14 24s14-14 14-24C29 7 23 1 15 1z" fill="var(--yellow)"/><circle cx="15" cy="15" r="8" fill="var(--white)"/></svg>
      No.53,<br>Linsen Rd.,<br>Beiyuan Dist.,<br>Tainan City 710
    </div>
  </div>

  <div class="offer-title">SPECIAL<br>OPENING OFFER</div>
  <div class="offer-deal">BUY 40 <b>TOKENS</b> GET 10 FREE</div>
  <div class="offer-ends">Offer Ends Septemebr 22nd</div>
  <div class="phone">
    <svg width="24" height="24" viewBox="0 0 24 24"><circle cx="12" cy="12" r="11" fill="none" stroke="var(--yellow)" stroke-width="2"/><path d="M8 6l2 3-1.5 1.5c.8 1.8 2.2 3.2 4 4L14 13l3 2-1 2.5c-4 0-9-5-9-9z" fill="var(--yellow)"/></svg>
    0958476201
  </div>
  <div class="footer-web">
    <svg width="14" height="14" viewBox="0 0 14 14"><circle cx="7" cy="7" r="6" fill="none" stroke="var(--yellow)" stroke-width="1.5"/><path d="M1 7h12M7 1c-3 3-3 9 0 12M7 1c3 3 3 9 0 12" fill="none" stroke="var(--yellow)" stroke-width="1"/></svg>
    www.briskpulsewkt.example
  </div>
  <div class="footer-follow">FOLLOW US <span class="dot"></span> BRISKPULSEWORKOUT</div>
</section>

<section class="flyer flyer--back">
  <div class="flyer__backdrop" role="img" aria-label="Dark photo of cardio machines in the gym"></div>
  <svg class="flyer__shapes" width="525" height="744" viewBox="0 0 525 744">
    <polygon points="0,0 525,0 525,140 0,282" fill="var(--yellow)"/>
    <polygon points="0,282 525,140 525,152 0,294" fill="#1a1a1a"/>
    <polygon points="0,690 525,595 525,744 0,744" fill="var(--red)"/>
    <polygon points="0,700 525,605 525,625 0,720" fill="var(--red-dark)" opacity=".6"/>
  </svg>

  <div class="brand-mark"></div>
  <div class="brand-name">Brisk Pulse Workout</div>
  <div class="brand-tagline">BUILD YOUR BODY - BUILD YOUR DREAMS</div>
  <div class="headline-first">WORLDS<br>FIRST</div>
  <div class="headline-coin">COIN <small>OPERATED</small></div>
  <div class="headline-center">CARDIO CENTER</div>
  <div class="badge-24"><span class="open">Open</span><span class="num">24</span><span class="hours">Hours</span></div>

  <div class="steps-photo" style="top:292px" role="img" aria-label="Hand inserting a bill into the yellow money changer"></div>
  <div class="steps-photo" style="top:410px;background:linear-gradient(135deg,#d8d8d8,#6d6d6d)" role="img" aria-label="Hand inserting a token into a machine timer"></div>
  <div class="steps-photo" style="top:530px;background:linear-gradient(135deg,#e9e3c0,#3e3e3e)" role="img" aria-label="People exercising on treadmills"></div>

  <div class="step" style="top:296px"><h3>STEP 1:</h3>Insert The Proper Bill Denomination Into The Money Changer For Your Tokens.</div>
  <div class="step" style="top:408px"><h3>STEP 2:</h3>Select The Machine That You Would Like To Use And Insert One Token Into The Timer For Every 20 Minutes Of Exercise.</div>
  <div class="step" style="top:546px"><h3>STEP 3:</h3>Relax And Enjoy Your Exercise.</div>

  <div class="phone">
    <svg width="28" height="28" viewBox="0 0 24 24"><circle cx="12" cy="12" r="11" fill="none" stroke="var(--yellow)" stroke-width="2"/><path d="M8 6l2 3-1.5 1.5c.8 1.8 2.2 3.2 4 4L14 13l3 2-1 2.5c-4 0-9-5-9-9z" fill="var(--yellow)"/></svg>
    0958476201
  </div>
  <div class="footer-follow">FOLLOW US <span class="dot"></span> BRISKPULSEWORKOUT</div>
  <div class="footer-web">
    <svg width="15" height="15" viewBox="0 0 14 14"><circle cx="7" cy="7" r="6" fill="none" stroke="var(--yellow)" stroke-width="1.5"/><path d="M1 7h12M7 1c-3 3-3 9 0 12M7 1c3 3 3 9 0 12" fill="none" stroke="var(--yellow)" stroke-width="1"/></svg>
    www.briskpulsewkt.example
  </div>
</section>

</body>
</html>
```